Business Card Design

We need a business card design for a business based in Perth Western Australia. We supply bookkeeping,office systems and procedures. This company is run by professional, vibrant woman which needs to come across when looking at this card.
This includes:
Bookkeeping,BAS,Super,Payroll,Group Certificates,Year End Preparation, Budgets,Planning
Staff training
Office Clean Up, Archiving,New Files and Systems
We would like to see designs that use the colours red mahogony(see Seal attachment), black and ivory
We want a Seal(old fashion wax seal) (see attached) with the letters TL engraved into this ,with our mission statement, 'We leave our mark of excellence'
Updates

Hi to all

Please note that Tidewell Ledgers e mail address should read:  tidewellledgers.wa@quillbox.net
Thanks

Industry/Entity Type

Fashion

Contact Information for Business Card

Tidewell Ledgers
Bookkeeping,Office Systems & Procedures
Perth WA
Freya
MOB: 0438 512 647
e mail: tidewellledgers@quillbox.net

```html
<!DOCTYPE html>
<html lang="en">
<head>
<meta charset="utf-8">
<title>Tidewell Ledgers – Business Card</title>
<link rel="stylesheet" href="https://fonts.googleapis.com/css2?family=Bebas+Neue&family=Open+Sans:wght@400&display=swap">
<style>
  :root {
    --backdrop: #a8a8a8;
    --card-black: #1a1717;
    --card-glow: #2a2222;
    --mahogany: #c0262b;
    --mahogany-deep: #8e1418;
    --ivory: #f4e9c6;
  }
  html, body {
    margin: 0;
    width: 1200px;
    height: 900px;
    overflow: hidden;
    background: var(--backdrop);
  }
  .stage {
    width: 1200px;
    height: 900px;
    display: flex;
    align-items: center;
    justify-content: center;
  }
  .business-card {
    position: relative;
    width: 900px;
    height: 514px;
    background:
      radial-gradient(circle at 230px 257px, var(--card-glow) 0, var(--card-black) 260px);
    box-shadow: 0 6px 18px rgba(0,0,0,0.25);
    overflow: hidden;
  }
  .seal-mark {
    position: absolute;
    left: 60px;
    top: 87px;
    width: 340px;
    height: 340px;
    border-radius: 50%;
    background: radial-gradient(circle at 45% 40%, var(--mahogany) 0, var(--mahogany) 55%, var(--mahogany-deep) 100%);
    display: flex;
    align-items: center;
    justify-content: center;
  }
  .seal-name {
    font-family: "Bebas Neue", sans-serif;
    font-size: 40px;
    color: var(--ivory);
    letter-spacing: 1px;
  }
  .card-details {
    position: absolute;
    left: 450px;
    top: 150px;
    color: var(--ivory);
  }
  .company-name,
  .contact-name {
    font-family: "Bebas Neue", sans-serif;
    font-weight: 400;
    margin: 0;
    line-height: 1;
  }
  .company-name { font-size: 44px; }
  .company-services {
    font-family: "Open Sans", sans-serif;
    font-size: 19px;
    margin: 4px 0 0 8px;
  }
  .contact-name {
    font-size: 40px;
    margin: 34px 0 0 20px;
  }
  .contact-line {
    font-family: "Open Sans", sans-serif;
    font-size: 19px;
    margin: 6px 0 0 28px;
  }
</style>
</head>
<body>
  <main class="stage">
    <section class="business-card">
      <div class="seal-mark">
        <span class="seal-name">Tidewell Ledgers</span>
      </div>
      <div class="card-details">
        <h1 class="company-name">TIDEWELL LEDGERS</h1>
        <p class="company-services">Bookkeeping, Office Systems &amp; Procedures</p>
        <h2 class="contact-name">PERTH WA FREYA</h2>
        <p class="contact-line">mobile: 0438 512 647</p>
        <p class="contact-line">email: tidewellledgers@quillbox.net</p>
      </div>
    </section>
  </main>
</body>
</html>
```